Webdesign für Beratung und Service im Bereich Heizungs- und Kühltechnologie
Zielgruppe
Wir sind ein modernes Dienstleistungsunternehmen, dass im Bereich Beratung und Service für Heizungs- und Kühltechnologie tätig ist. Wir suchen ein modernes Webdesign, das sich überwiegend an Geschäfts- / Gewerbekunden richten soll.
Aufgabenstellung
Wir möchten die in unserem Logo verwendete Farben auf der Webseite wiederfinden, Bilder werden mitgeliefert, müssen aber keine Verwendung finden. Wichtig ist das Hervorheben als Kundendienstvertretung des Premium-Herstellers BRK mit deren Logo und direktem Link auf deren Webseite. Gerne würden wir einen modernen Ansatz sehen, abweichend von den Standard-Seiten anderer Wartungsfirmen in unserer Branche.

```html
<!DOCTYPE html>
<html lang="de">
<head>
<meta charset="utf-8">
<title>Thermvia – Heizungs- und Kühltechnologie</title>
<link href="https://fonts.googleapis.com/css2?family=Open+Sans:ital,wght@0,400;0,600;0,700;0,800;1,700&display=swap" rel="stylesheet">
<style>
:root{
  --navy:#1b3a6b;
  --navy-dark:#133566;
  --red:#d3202b;
  --dark-red:#9e1c22;
  --band:#c6cdd8;
  --text:#1d2f55;
  --muted:#6b7280;
  --line:#2a4a80;
  --white:#fff;
}
*{box-sizing:border-box;margin:0;padding:0}
html,body{width:1200px;height:2312px;overflow:hidden;background:var(--white)}
body{position:relative;font-family:"Open Sans",Arial,sans-serif;color:var(--text)}
.abs{position:absolute}

/* header */
.site-header{left:0;top:0;width:1200px;height:56px;background:var(--white)}
.brand{left:237px;top:10px;display:flex;align-items:center;gap:8px}
.brand-dot{width:20px;height:20px;border-radius:50%;background:var(--navy)}
.brand-name{font-weight:700;font-size:22px;color:var(--navy)}
.tagline{left:376px;top:15px;font-weight:600;font-size:11.5px;line-height:15px;color:var(--navy);text-align:center}
.topline{left:727px;top:9px;font-size:7px;color:var(--navy);display:flex;gap:28px}
.topline .alert{color:var(--red);font-weight:700}
.main-nav{left:650px;top:32px;display:flex;gap:15px;font-size:9.5px;color:#555}
.main-nav .active{color:var(--navy);font-weight:700}

/* hero */
.hero{left:0;top:56px;width:1200px;height:562px;background:linear-gradient(135deg,#b9bcc0,#e4e6e8 40%,#a9adb2 70%,#d6d8db)}
.hero-title{left:249px;top:132px;font-weight:800;font-size:30px;line-height:38px;color:var(--navy);text-transform:uppercase}
.btn-alert{left:277px;top:319px;width:162px;height:27px;background:var(--red);color:#fff;font-weight:700;font-size:18px;display:flex;align-items:center;gap:8px;padding-left:8px;letter-spacing:.5px}

/* band + cards */
.band{left:0;top:903px;width:1200px;height:249px;background:var(--band)}
.card{top:569px;width:226px;height:385px;background:#fff;border:1px solid var(--line);text-align:center;padding:18px 14px 0}
.card h2{font-size:19px;font-weight:600;color:var(--navy);margin:6px 0 12px}
.card p{font-size:8.6px;line-height:13.8px;color:var(--text)}
.card .gap{height:13.8px}
.icon{height:40px;display:flex;justify-content:center;align-items:center}
.partner-mark{font-weight:700;font-size:26px;color:var(--red)}

.product{top:970px;width:205px;height:295px}
.p1{left:247px;background:linear-gradient(160deg,#3a3a3c,#1f1f21 60%,#555)}
.p2{left:489px;background:linear-gradient(160deg,#e8e9eb,#bfc2c6 60%,#d9dbde)}
.p3{left:740px;background:linear-gradient(160deg,#8a8862,#6e6c4b 60%,#9c9a77)}

/* emergency */
.emergency{left:0;top:1294px;width:1200px;text-align:center}
.emergency h3{display:flex;justify-content:center;align-items:center;gap:10px;font-size:20px;font-weight:600;color:var(--dark-red)}
.emergency p{font-size:8.8px;line-height:14px;margin-top:2px}
.emergency strong{font-weight:700}

/* contact */
.contact-title{left:0;top:1396px;width:1200px;text-align:center;font-size:19px;font-weight:600;color:var(--dark-red)}
.contact-intro{left:236px;top:1428px;font-size:9px;display:flex;align-items:center;gap:5px}
.box{display:inline-block;width:10px;height:10px;border:1px solid var(--line);background:#fff}
.field{top:1455px;width:131px;height:18px;border:1px solid var(--line);font-size:6.5px;color:#777;padding:4px 8px}
.hint{left:255px;top:1485px;font-size:6.5px;color:#555}
.req{left:827px;top:1485px;font-size:6.5px;color:#555}
.textarea{left:244px;top:1503px;width:417px;height:40px;border:1px solid var(--line)}
.consent{left:255px;top:1553px;display:flex;gap:8px;font-size:6.5px;line-height:11px;color:#555;width:370px}
.consent .box{flex:none;margin-top:4px;width:11px;height:11px}
.submit{left:675px;top:1556px;width:100px;height:19px;background:var(--navy);color:#fff;font-size:10.5px;font-weight:600;display:flex;align-items:center;justify-content:center}

/* footer */
.footer{left:0;top:1610px;width:1200px;height:125px;background:var(--navy-dark);color:#fff}
.foot-links{left:380px;top:26px;font-size:7.5px;font-weight:600;line-height:13.3px}
.foot-logo{left:487px;top:29px;width:139px;height:45px;background:#fff;display:flex;align-items:center;justify-content:center;gap:6px}
.foot-logo .brand-dot{width:14px;height:14px}
.foot-logo .brand-name{font-size:17px}
.foot-tag{left:487px;top:80px;width:139px;text-align:center;font-size:9.5px;font-weight:700;line-height:15px}
.foot-col{top:20px;font-size:7.3px;font-weight:600;line-height:13.3px}
.cookie{left:0;top:1697px;width:1200px;height:38px;background:rgba(160,172,190,.82);display:flex;align-items:center;justify-content:flex-end;padding-right:22px;gap:12px}
.cookie p{font-size:8.6px;color:var(--navy)}
.cookie .ok{width:36px;height:28px;background:var(--navy-dark);color:#fff;font-weight:800;font-size:14px;display:flex;align-items:center;justify-content:center;letter-spacing:1px}

/* mobile screen */
.mobile{left:244px;top:1790px;width:201px;height:382px;background:#fff;overflow:hidden;border:1px solid #ddd}
.m-top{height:18px;font-size:6px;display:flex;justify-content:flex-end;align-items:center;padding-right:8px;gap:3px}
.m-top .alert{color:var(--red);font-weight:700}
.m-hero{height:125px;background:linear-gradient(135deg,#9ea2a7,#d6d8da 45%,#8c9095)}
.m-btn{position:absolute;left:33px;top:137px;width:130px;height:21px;background:var(--red);color:#fff;font-weight:700;font-size:14px;display:flex;align-items:center;gap:5px;padding-left:6px}
.m-title{margin-top:30px;text-align:center;font-size:13px;font-weight:600;line-height:19px;color:var(--navy)}
.m-icon{display:flex;justify-content:center;margin-top:12px}
.m-h{text-align:center;font-size:13px;font-weight:600;color:var(--navy);margin-top:2px}
.m-p{text-align:center;font-size:9px;line-height:13px;padding:0 8px;margin-top:2px}
.m-bar{position:absolute;left:0;bottom:0;width:100%;height:22px;background:var(--navy-dark);color:#fff;display:flex;align-items:center;justify-content:space-between;padding:0 12px;font-size:9px;font-weight:700;letter-spacing:2px}
.m-bar .pill{background:#fff;color:var(--navy);border-radius:10px;font-size:7px;letter-spacing:0;padding:2px 10px}

.preview{left:599px;top:1774px;width:313px;height:235px;background:linear-gradient(135deg,#8f9398,#d8dadc 45%,#7f8388 80%,#b5b8bc)}
.caption{left:631px;top:2024px;font-size:9px;color:#666}
.note{left:490px;top:2155px;font-size:7px;line-height:10px;color:#9b2f8a}
</style>
</head>
<body>

<header class="site-header abs">
  <div class="brand abs"><span class="brand-dot"></span><span class="brand-name">Thermvia</span></div>
  <div class="tagline abs">HIGH EFFICIENT HEATING<br>AND COOLING SERVICE</div>
  <div class="topline abs"><span>✉ info@thermvia.de</span><span><span class="alert">Notdienst</span> +49 (0) 8123 4567890 10</span></div>
  <nav class="main-nav abs"><span class="active">Home</span><span>Über uns</span><span>Kundendienst</span><span>Wartung</span><span>Notdienst</span><span>Kontakt</span></nav>
</header>

<section class="hero abs" role="img" aria-label="Foto: Edelstahl-Rohrleitungen und Plattenwärmetauscher"></section>
<h1 class="hero-title abs">Ihr Spezialist für<br>Beratung und Service<br>im Bereich der<br>Heizungs- und Kühltechnologie</h1>
<div class="btn-alert abs">
  <svg width="22" height="22" viewBox="0 0 24 24" fill="none" stroke="#fff" stroke-width="1.6"><circle cx="15" cy="9" r="6"/><path d="M4 6c0 8 6 14 14 14l1-3-3-2-2 2c-3-1-6-4-7-7l2-2-2-3z"/><text x="12" y="11" font-size="6" fill="#fff" stroke="none" font-family="Arial">24</text></svg>
  NOTDIENST
</div>

<div class="band abs"></div>

<article class="card abs" style="left:237px">
  <div class="icon"><svg width="40" height="38" viewBox="0 0 40 38" fill="none" stroke="#d3202b" stroke-width="2.4"><path d="M4 18 20 4l16 14"/><path d="M9 14v21h22V14"/><path d="M16 35V24h8v11"/></svg></div>
  <h2>Über uns</h2>
  <p>Wir sind ein modernes Beratungs- und Service-Unternehmen mit hochmotivierten Mitarbeitern, die seit Jahrzehnten in der Heizungs- und Klimabranche tätig sind. Unsere Mitarbeiter sind stets auf den neuesten Stand der Technik geschult. Verteilte Servicestationen machen es möglich, dass wir Ihnen deutschlandweit an 365 Tagen / 24 Stunden unsere Dienste anbieten können.</p>
  <div class="gap"></div>
  <p>Optimierte Einsatzplanung garantieren Ihnen schnelle Reaktionszeiten und schlanke Prozessstrukturen sorgen für eine reibungslose Ersatzteilversorgung. Profitieren Sie von dem tiefgreifenden Know-How unsere Mitarbeiter, ihren langjährigen Erfahrungen und dem hohen Qualitätsanspruch unseres Unternehmens.</p>
</article>

<article class="card abs" style="left:487px">
  <div class="icon"><span class="partner-mark">BRK</span></div>
  <h2>Kundendienst</h2>
  <p>In unserem Fokus stehen Heizungs- und Kühltechnologie mit hoher Effizienz und Rückhaltigkeit.<br>Als Kundendienstvertretung des <b><i>Schweizer Premium-Herstellers BRK</i></b>, übernehmen wir alle Kundendienstleistungen für Inbetriebnahmen, Gewährleistungs- Wartungs- und Servicearbeiten für deren Produktportfolio (u.a. Luft-Wasser oder Sole-Wasser Wärmepumpen, Splitgeräte und Serverraumkühlungen).</p>
  <div class="gap"></div>
  <p><b>Außerdem bieten wir Service und Wartungsarbeiten für folgende Produkte an:</b><br>• Klimaanlagen der Firma Nordklima<br>• Varo-Wärmepumpen<br>• Heizungswartungen und Austausch an Heizwerk, Thermalon, Calorix etc.<br>• Solaranlagen<br>• BHKW der Firmen KWM und Enerbau</p>
</article>

<article class="card abs" style="left:737px">
  <div class="icon"><svg width="40" height="38" viewBox="0 0 40 38" fill="none" stroke="#d3202b" stroke-width="2.4" stroke-linecap="round"><path d="M6 34 30 10"/><path d="M27 4a7 7 0 0 0 7 9l-4 1-4-4z"/><path d="M8 6l6 6M11 11l21 21"/><path d="M4 4l5 1 1 5"/></svg></div>
  <h2>Wartung-Service</h2>
  <p>• Sorgt für einen störungsfreien Regel-Betrieb<br>• Steht für eine optimale Energiebilanz<br>• Verlängert die Lebensdauer Ihrer Anlage<br>• Erfüllt die gesetzl. Betriebsanforderungen</p>
  <div class="gap"></div>
  <p><b>Unsere Wartungs-Service umfasst:</b><br>• Kontrolle des gesamten Systems<br>• Austausch von Verschleißteilen<br>• Einstellung der Betriebsparameter<br>• Erkennen von Fehlern bevor diese ein Problem werden<br>• Sauberes, Arbeiten und transparente Information an den Kunden</p>
  <div class="gap"></div>
  <p>Wartungsverträge nach FTMA schaffen Sicherheit und Vertrauen.<br>Entscheiden Sie sich für den Spezialisten und lassen Sie sich ein individuelles Angebot für Ihre Anlagen erstellen</p>
</article>

<div class="product p1 abs" role="img" aria-label="Produktfoto: Wärmepumpe mit offener Front und Kupferleitungen"></div>
<div class="product p2 abs" role="img" aria-label="Produktfoto: silberne Außeneinheit einer Wärmepumpe"></div>
<div class="product p3 abs" role="img" aria-label="Produktfoto: olivfarbene Kältemaschine mit Ventilator"></div>

<section class="emergency abs">
  <h3><svg width="36" height="36" viewBox="0 0 24 24" fill="none" stroke="#9e1c22" stroke-width="1.2"><circle cx="15" cy="9" r="6"/><path d="M4 6c0 8 6 14 14 14l1-3-3-2-2 2c-3-1-6-4-7-7l2-2-2-3z"/><text x="11.6" y="11" font-size="5.5" fill="#9e1c22" stroke="none" font-family="Arial">24</text></svg>Notdienst +49 (0) 8123 4567890 10</h3>
  <p>Unser Notdienst steht Ihnen rund-um die Uhr für folgende Leistungen zur Verfügung:<br>Identifizieren und Beheben von Betriebs-Störungen an:<br><strong>• Wärmepumpen &nbsp;&nbsp;• Heizungsanlagen &nbsp;&nbsp;• Klimaanlagen &nbsp;&nbsp;• Solaranlagen</strong></p>
</section>

<h2 class="contact-title abs">Kontakt zu uns</h2>
<div class="contact-intro abs">Bitte nehmen Sie zu mit / uns unverbindlich Kontakt auf, wir möchte uns beraten lassen zu Ihren <span class="box"></span> BRK-Servicearbeiten <span class="box"></span> BRK-Wartungsarbeiten <span class="box"></span> sonstiger Hersteller</div>
<div class="field abs" style="left:245px">Name, Vorname*</div>
<div class="field abs" style="left:386px">Firma*</div>
<div class="field abs" style="left:529px">E-Mailadresse*</div>
<div class="field abs" style="left:674px">Tel. / Handy*</div>
<div class="field abs" style="left:820px">Gerätestandort</div>
<div class="hint abs">Bitte teilen Sie uns in Ihrer Nachricht nach Möglichkeit genauer Informationen zu Hersteller, Gerätetyp, Baujahr, Garantie und / oder Mängel mit.</div>
<div class="req abs">*Pflichtfelder</div>
<div class="textarea abs"></div>
<div class="consent abs"><span class="box"></span><span>Ich habe die <u>Datenschutzerklärung</u> zur Kenntnis genommen und akzeptiert. Ich stimme zu, dass meine Formularangaben zur Kontaktaufnahme bzw. zur Bearbeitung meines Anliegens gespeichert werden.</span></div>
<div class="submit abs">abschicken &gt;</div>

<footer class="footer abs">
  <div class="foot-links abs">Home<br>Kontakt<br>Impressum<br>AGB<br>Datenschutz<br>Cookie-Policy</div>
  <div class="foot-logo abs"><span class="brand-dot"></span><span class="brand-name">Thermvia</span></div>
  <div class="foot-tag abs">HIGH EFFICIENT HEATING<br>AND COOLING SERVICE</div>
  <div class="foot-col abs" style="left:689px">FIRMENSITZ<br>Thermvia GmbH<br>Lindenweg 5b<br>85600 Musterhofen<br><br>Tel. +49 (0) 8123 4567890 10 - Fax +49 (0) 8123 4567890 11<br>info@thermvia.de</div>
  <div class="foot-col abs" style="left:819px">SERVICE ZENTRALE<br>Thermvia GmbH<br>Amselweg 1<br>37400 Talbach</div>
</footer>
<div class="cookie abs"><p>Um unsere Webseite für Sie optimal zu gestalten und fortlaufend verbessern zu können, verwenden wir Cookies. Durch die weitere Nutzung der Webseite stimmen Sie der Verwendung von Cookies zu.</p><span class="ok">OK</span></div>

<section class="mobile abs">
  <div class="m-top"><span class="alert">Notdienst</span> +49 (0) 8123 4567890 10</div>
  <div class="m-hero" role="img" aria-label="Foto: Edelstahl-Rohrleitungen und Plattenwärmetauscher"></div>
  <div class="m-btn">
    <svg width="16" height="16" viewBox="0 0 24 24" fill="none" stroke="#fff" stroke-width="1.6"><circle cx="15" cy="9" r="6"/><path d="M4 6c0 8 6 14 14 14l1-3-3-2-2 2c-3-1-6-4-7-7l2-2-2-3z"/></svg>NOTDIENST
  </div>
  <div class="m-title">Ihr Spezialist für<br>Beratung und Service<br>im Bereich der<br>Heizungs- und Kühltechnologie</div>
  <div class="m-icon"><svg width="32" height="30" viewBox="0 0 40 38" fill="none" stroke="#d3202b" stroke-width="2.4"><path d="M4 18 20 4l16 14"/><path d="M9 14v21h22V14"/><path d="M16 35V24h8v11"/></svg></div>
  <div class="m-h">Über uns</div>
  <div class="m-p">Wir sind ein modernes Beratungs- und Service-Unternehmen mit hochmotivierten</div>
  <div class="m-bar"><span>☰ MENU</span><span class="pill">Thermvia</span></div>
</section>

<div class="preview abs" role="img" aria-label="Foto: Edelstahl-Rohrleitungen und Plattenwärmetauscher"></div>
<div class="caption abs">Originalbild</div>
<div class="note abs">&lt; Menu unten = ergonomischer und<br>&nbsp;&nbsp;das Logo nimmt oben nicht wichtigen<br>&nbsp;&nbsp;Contentplatz weg</div>

</body>
</html>
```